Harwick Recovery Centre Tailormade Training

We are wanting to promote our Training Unit and in particular tailor made training. We want our name - Harwick Recovery Centre - to be prominent and to include the bullet points from attached file plus other content as seems useful from the file. We need the PCS logo and Trust name at the bottom using PCS blue - other modern colours to blend in with this. Some graphics and modern design. Overall message: quality training at reasonable cost tailored to agency needs.

Target Market(s)

Agencies providing services for people with alcohol and drug problems

Industry/Entity Type

Health Care

Font styles to use
Sans Serif

Colors
f37122
85cae6
fbf289

Requirements
Must have
• Harwick Recovery Centre
• We will......
•  Support your organisation to develop a training plan and work with you to design the course content.
•  Assign a member of our team to liaise with you through- out the programme.
•  Provide experienced and qualified teaching staff to de- liver your training.
• For further information and prices please contact
• Colin Marsby, Training Department Manager
• Harwick Recovery Centre, 42 Brackenhill Row, Leeds LS7 3QD telephone 0113 4720368 hrc@vantorel.ac.uk
• PCS logo with Trust name - see bottom of attached file - use exact PCS blue
Nice to have
• Modern colours to tone with PCS blue
• Some graphics or bold background
• Emphasis is on the training but needs a connection to addictions
Should not have
• Nothing stereotyped of problem drinkers or drug users

```html
<!DOCTYPE html>
<html lang="en">
<head>
<meta charset="utf-8">
<title>Harwick Recovery Centre Training</title>
<link rel="stylesheet" href="https://fonts.googleapis.com/css2?family=Oswald:wght@600;700&family=Roboto+Condensed:wght@300;400;700&family=Roboto+Slab:wght@900&family=Yellowtail&display=swap">
<style>
  :root{
    --sky-top:#63b9da;
    --sky-bottom:#9fd6ea;
    --sun-light:#fde08a;
    --sun-deep:#fcc23a;
    --trust-blue:#005eb8;
    --panel-blue:#0a8bc5;
    --heading-blue:#0b78b3;
    --ink:#3b3b3d;
    --body-ink:#33302a;
    --white:#ffffff;
    --dot:#fcc23a;
  }
  *{margin:0;padding:0;box-sizing:border-box}
  html,body{width:846px;height:1200px;overflow:hidden;background:#fff}
  .poster{position:relative;width:846px;height:1200px;overflow:hidden;font-family:"Roboto Condensed",sans-serif}

  .masthead{position:absolute;left:0;top:0;width:846px;height:286px;
    background:linear-gradient(180deg,var(--sky-top) 0%,var(--sky-bottom) 100%)}
  .masthead__name{position:absolute;left:0;top:22px;width:846px;text-align:center;
    font-family:"Oswald",sans-serif;font-weight:700;font-size:70px;line-height:84px;
    color:var(--white);letter-spacing:1px}
  .masthead__title{position:absolute;left:0;top:100px;width:846px;text-align:center;
    font-family:"Roboto Slab",serif;font-weight:900;font-size:88px;line-height:96px;
    color:var(--ink);letter-spacing:3px}
  .masthead__intro{position:absolute;left:204px;top:194px;width:479px;
    font-size:15px;line-height:20px;color:var(--white);text-align:justify}
  .masthead__intro strong{color:var(--ink);font-weight:400}

  .offer{position:absolute;left:0;top:286px;width:846px;height:340px;
    background:linear-gradient(90deg,var(--sun-light) 0%,var(--sun-deep) 100%)}
  .features{position:absolute;left:73px;top:10px;width:345px}
  .feature{margin-bottom:9px}
  .feature__head{font-family:"Oswald",sans-serif;font-weight:600;font-size:19px;line-height:24px;color:var(--heading-blue)}
  .feature__text{font-size:15.5px;line-height:22px;color:var(--body-ink);font-weight:300}

  .pledge__title{position:absolute;left:424px;top:-6px;font-family:"Yellowtail",cursive;
    font-size:66px;line-height:90px;color:var(--heading-blue)}
  .pledge__box{position:absolute;left:442px;top:84px;width:334px;height:232px}
  .pledge__box svg{position:absolute;left:0;top:0}
  .pledge__list{position:absolute;left:22px;top:10px;width:300px;list-style:none}
  .pledge__list li{position:relative;padding-left:16px;margin-bottom:12px;
    font-size:16px;line-height:22px;color:var(--white);font-weight:300}
  .pledge__list li::before{content:"";position:absolute;left:2px;top:8px;width:7px;height:7px;border-radius:50%;background:var(--dot)}

  .imagery{position:absolute;left:0;top:626px;width:846px;height:451px}
  .tile{position:absolute}
  .tile--balcony{left:0;top:0;width:276px;height:222px;background:linear-gradient(120deg,#8a7f70,#c9c2b5 60%,#6f655a)}
  .tile--bench{left:276px;top:0;width:291px;height:222px;background:radial-gradient(circle at 55% 25%,#f3f1ea 0%,#9b8f7a 40%,#2c2620 80%)}
  .tile--shout{left:567px;top:0;width:279px;height:222px;background:linear-gradient(135deg,#dcdbd6,#a8a49c 60%,#c9c6bf)}
  .tile--glass{left:0;top:222px;width:276px;height:229px;background:linear-gradient(150deg,#7a5a4a,#c7b9ad 50%,#5b4233)}
  .tile--tunnel{left:276px;top:222px;width:291px;height:229px;background:radial-gradient(ellipse at 50% 55%,#f2f4f2 0%,#7d8688 30%,#1e2224 75%)}
  .tile--fist{left:567px;top:222px;width:279px;height:229px;background:radial-gradient(circle at 45% 50%,#b58d78 0%,#9aa0a2 45%,#7d8487 100%)}

  .footer{position:absolute;left:0;top:1077px;width:846px;height:123px;background:var(--panel-blue)}
  .footer__trust{position:absolute;left:0;top:0;width:276px;height:123px;background:var(--white)}
  .footer__trust-name{position:absolute;left:16px;top:42px;width:250px;
    font-family:"Roboto Condensed",sans-serif;font-weight:700;font-size:15px;line-height:18px;color:var(--trust-blue)}
  .footer__contact{position:absolute;left:296px;top:10px;width:252px;text-align:center;
    font-size:14.5px;line-height:20.5px;color:var(--white);font-weight:300}
  .footer__rule{position:absolute;left:567px;top:10px;width:1px;height:98px;background:rgba(255,255,255,.7)}
  .footer__address{position:absolute;left:580px;top:10px;width:254px;text-align:center;
    font-size:14.5px;line-height:20.5px;color:var(--white);font-weight:300}
  .footer__address strong{font-weight:700}
</style>
</head>
<body>
<div class="poster">
  <header class="masthead">
    <h1 class="masthead__name">HARWICK RECOVERY CENTRE</h1>
    <div class="masthead__title">TRAINING</div>
    <p class="masthead__intro"><strong>Your organisation may require training for health and social care professionals</strong> concerned with the management of substance misuse issues. We can address your specific needs, with the location, timing and course content designed to suit your training objectives.</p>
  </header>

  <section class="offer">
    <div class="features">
      <div class="feature">
        <h2 class="feature__head">TAILORED CONTENT</h2>
        <p class="feature__text">Work with us to develop a course that meets your specific requirements.</p>
      </div>
      <div class="feature">
        <h2 class="feature__head">CONFIDENTIAL</h2>
        <p class="feature__text">Staff can explore issues relevant to your<br>area of work.</p>
      </div>
      <div class="feature">
        <h2 class="feature__head">FLEXIBLE</h2>
        <p class="feature__text">Hold the course at a convenient time for your service and spread the training over a series of sessions, days or months.</p>
      </div>
      <div class="feature">
        <h2 class="feature__head">LOCATION</h2>
        <p class="feature__text">Bring the course in-house or use our fully serviced training facility.</p>
      </div>
    </div>

    <div class="pledge__title">We will</div>
    <div class="pledge__box">
      <svg width="334" height="232" viewBox="0 0 334 232" aria-hidden="true">
        <polygon points="0,0 286,0 334,48 334,232 42,232 0,182" fill="var(--panel-blue)"/>
      </svg>
      <ul class="pledge__list">
        <li>Support your organisation to develop a training plan and work with you to design the course content.</li>
        <li>Assign a member of our team to liaise with you throughout the programme.</li>
        <li>Provide experienced and qualified teaching staff to deliver your training.</li>
      </ul>
    </div>
  </section>

  <section class="imagery">
    <div class="tile tile--balcony" role="img" aria-label="Photo of a man leaning on a balcony rail, head resting on his arm"></div>
    <div class="tile tile--bench" role="img" aria-label="Photo of a silhouetted figure sitting on a park bench, head in hands"></div>
    <div class="tile tile--shout" role="img" aria-label="Photo of a man shouting in frustration"></div>
    <div class="tile tile--glass" role="img" aria-label="Photo of a tipped-over spirits bottle beside a glass"></div>
    <div class="tile tile--tunnel" role="img" aria-label="Photo of a person walking through a dark tunnel towards the light"></div>
    <div class="tile tile--fist" role="img" aria-label="Photo of a fist breaking through a wall"></div>
  </section>

  <footer class="footer">
    <div class="footer__trust">
      <div class="footer__trust-name">Wharfe and Calder Partnership<br>PCS Foundation Trust</div>
    </div>
    <p class="footer__contact">For further information<br>and prices please contact<br>Colin Marsby,<br>Training Department Manager</p>
    <div class="footer__rule"></div>
    <p class="footer__address">Harwick Recovery Centre,<br>42 Brackenhill Row,<br>Leeds LS7 3QD<br>Telephone <strong>0113 4720368</strong>,<br>hrc@vantorel.ac.uk</p>
  </footer>
</div>
</body>
</html>
```